Facial Cosmetic Business Card Design

I am a Physician certified in Lumivex injections, Sorelane fillers,& Chemical Peels.
I do no surgery
I have 20 years experience in facial cosmetics
30+ years medical experience
name is not TM but thought something like "Radiant Visage" catches what I do and the look I get with minimal to no downtime and no recovery time.
I do home parties and also private home consultations and treatments in a relaxed atmosphere with no pressure.
Aestheology services upon referral to a private associate as well.
I have no logo, photo's or desigs so I am ope to suggestions

To all the MD is my medical degree

the MNGGC are my board certifications stands for Member National Guild General Care
4816 Cedar Hollow Lane is my office home address
4045518832 is my cell/office number or contact info

Thanks

Reason: Sorry was out of town I like a few of the designs so I have enough to choose from set tweeks to be done with prof degree and address mixup. Once i see corrections I will choose approp one thanks all Dr Kessler

Target Market(s)

mostly wome do these procedures usually i the above 35 crowd certainly over 40 crowd for sure

Industry/Entity Type

Medical

Contact Information for Business Card

Radiant Visage, Daniel Kessler MD, MNGGC
4816 Cedar Hollow Lane
Ashbury, GA. 30517
O:404-551-9016
C:404-551-8832
F:404-551-9070

```html
<!DOCTYPE html>
<html lang="en">
<head>
<meta charset="utf-8">
<title>Radiant Visage – Business Card</title>
<link rel="stylesheet" href="https://fonts.googleapis.com/css2?family=Marcellus+SC&family=Kalam:wght@400&display=swap">
<style>
  :root {
    --backdrop: #d9d9d9;
    --card-black: #050505;
    --brand-pink: #c871b4;
    --accent-blue: #4fb6e6;
    --text-white: #ffffff;
  }
  * { margin: 0; padding: 0; box-sizing: border-box; }
  html, body {
    width: 1200px; height: 900px; overflow: hidden;
    background: var(--backdrop);
  }
  .stage {
    width: 1200px; height: 900px;
    display: flex; align-items: center; justify-content: center;
  }
  .business-card {
    position: relative;
    width: 1000px; height: 572px;
    background: var(--card-black);
    overflow: hidden;
    font-family: "Marcellus SC", serif;
    color: var(--text-white);
    box-shadow: 0 10px 30px rgba(0,0,0,.25);
  }
  .brand-ribbon {
    position: absolute; left: 0; top: 62px;
    width: 560px; height: 110px;
  }
  .brand-name {
    position: absolute; left: 48px; top: 106px;
    font-size: 40px; font-weight: 400; letter-spacing: 2px;
    line-height: 48px;
    color: var(--text-white);
    white-space: nowrap;
  }
  .doctor-name {
    position: absolute; left: 70px; top: 190px;
    font-size: 40px; font-weight: 400; letter-spacing: 3px;
    line-height: 48px;
    color: var(--brand-pink);
    white-space: nowrap;
  }
  .credentials {
    position: absolute; left: 70px; top: 250px;
    font-size: 34px; line-height: 48px; letter-spacing: 1px;
    white-space: nowrap;
  }
  .hero-art {
    position: absolute; left: 640px; top: 30px;
    width: 300px; height: 330px;
    border-radius: 40% 40% 30% 30%;
    background: linear-gradient(100deg, rgba(200,113,180,.55) 0%, #141414 35%, #141414 70%, rgba(79,182,230,.55) 100%);
  }
  .tagline {
    position: absolute; left: 630px; top: 370px;
    width: 330px; text-align: center;
    font-family: "Kalam", cursive;
    font-size: 18px; line-height: 24px; color: var(--text-white);
    white-space: nowrap;
  }
  .contact-band {
    position: absolute; height: 28px;
    background: var(--brand-pink);
    display: flex; align-items: center;
    font-size: 18px; letter-spacing: 3px;
    color: var(--text-white);
    white-space: nowrap;
  }
  .contact-band--upper { left: 420px; right: 0; top: 408px; justify-content: flex-end; padding-right: 40px; }
  .contact-band--lower { left: 0; right: 0; bottom: 38px; padding-left: 60px; }
  .contact-cell {
    position: absolute; left: 470px; top: 452px;
    font-size: 18px; line-height: 24px; letter-spacing: 3px;
    color: var(--brand-pink);
    white-space: nowrap;
  }
</style>
</head>
<body>
<main class="stage">
  <article class="business-card">
    <svg class="brand-ribbon" viewBox="0 0 560 110" aria-hidden="true">
      <path d="M0 40 L440 40 Q480 38 520 4 L504 34 L556 30 Q500 80 440 96 L0 96 Z" fill="var(--brand-pink)"/>
    </svg>
    <h1 class="brand-name">Radiant Visage</h1>
    <h2 class="doctor-name">Daniel Kessler</h2>
    <p class="credentials">MD, MNGGC.<br>4816 Cedar Hollow Lane,<br>Ashbury,<br>Ga. 30517.</p>
    <div class="hero-art" role="img" aria-label="Illustration area: stylised portrait with flowing pink and blue hair lines"></div>
    <p class="tagline">"Let Your Confidence Shine Through"</p>
    <div class="contact-band contact-band--upper">Fax:404-551-9070</div>
    <p class="contact-cell">Cell:404-551-8832</p>
    <div class="contact-band contact-band--lower">Office:404-551-9016</div>
  </article>
</main>
</body>
</html>
```